Design and Renovation Company Luxury Business Card

I want to create a luxury business card for a Design and Renovation Firm . We will use our current logo. The company name is 742BUILD. We do not want anything standard. We need a very unique concept.
Please see uploaded inspiration. I really like the textured paper option. I would like the card to be thick with debossing, and/or embossing options. The logo has orange in it but I would like to see the card with and without the orange. I think the orange may make the company feel less high-end. The goal is to elevate the logo not match its vibe per se of the logo. We want something very unique, not standard at all!
I would like a space for :
Logo,
Name,
Position,
Email,
Office number,
Website Address,
Business Address,
Thank you!
Have fun!
Target Market(s)
Home owners Age 35 +
Industry/Entity Type
Design and Renovation
Contact Information for Business Card
Logo, Name, Position, Email, Office number, Website Address, Business Address,.
Colors
Designer to choose colors to be used in the design.
Requirements
Must have
- A luxury designer feel. Must be black or dark grey but open to other luxury ideas.
Nice to have
- Gold, silver, black embossing or debossing. Textured paper design.
Should not have
- A cheap look and feel.

```html
<!DOCTYPE html>
<html lang="en">
<head>
<meta charset="utf-8">
<title>742BUILD Business Card</title>
<link href="https://fonts.googleapis.com/css2?family=Montserrat:wght@500;700&family=Roboto:wght@400&display=swap" rel="stylesheet">
<style>
  :root {
    --backdrop: #4b4c4e;
    --card-black: #0d0d0e;
    --card-edge: #1c1c1e;
    --gold: #d4a82a;
    --gold-soft: #c9a03a;
  }
  * { margin: 0; padding: 0; box-sizing: border-box; }
  html, body { width: 1200px; height: 900px; overflow: hidden; }
  body {
    background: var(--backdrop);
    position: relative;
    font-family: "Roboto", Arial, sans-serif;
  }
  .card {
    position: absolute;
    width: 560px;
    height: 320px;
    background: var(--card-black);
    border: 1px solid var(--card-edge);
    border-radius: 4px;
    box-shadow: 0 18px 40px rgba(0,0,0,0.45);
    overflow: hidden;
  }
  .card-front { left: 70px; top: 90px; }
  .card-back { left: 570px; top: 490px; }

  /* front */
  .holder { position: absolute; left: 48px; top: 52px; }
  .holder-name {
    font-family: "Montserrat", Arial, sans-serif;
    font-weight: 700;
    font-size: 26px;
    color: var(--gold);
    letter-spacing: 0.5px;
  }
  .holder-position {
    font-family: "Montserrat", Arial, sans-serif;
    font-weight: 500;
    font-size: 15px;
    color: var(--gold-soft);
    letter-spacing: 3px;
    margin-top: 2px;
  }
  .brand-name {
    position: absolute;
    font-family: "Montserrat", Arial, sans-serif;
    font-weight: 500;
    color: var(--gold);
    letter-spacing: 2px;
    line-height: 1;
    white-space: nowrap;
  }
  .card-front .brand-name { left: 48px; top: 184px; font-size: 28px; }

  .contact {
    position: absolute;
    left: 318px; top: 170px;
    list-style: none;
    color: var(--gold);
    font-size: 14px;
    line-height: 19px;
  }
  .contact li { display: flex; align-items: flex-start; gap: 8px; }
  .contact svg { width: 12px; height: 12px; margin-top: 3px; flex: none; fill: var(--gold); }
  .contact .address-line { padding-left: 20px; }

  /* back */
  .texture {
    position: absolute; inset: 0;
    background: radial-gradient(ellipse at 45% 55%, #1f1f21 0%, #121213 55%, #0b0b0c 100%);
  }
  .card-back .brand-name {
    left: 50%; top: 50%;
    transform: translate(-50%, -50%);
    font-size: 44px;
    letter-spacing: 4px;
  }
</style>
</head>
<body>

<section class="card card-front">
  <div class="holder">
    <p class="holder-name">YOUR NAME</p>
    <p class="holder-position">POSITION</p>
  </div>

  <p class="brand-name">742BUILD</p>

  <ul class="contact">
    <li>
      <svg viewBox="0 0 12 12"><path d="M0 2h12v8H0z M1 3l5 3.5L11 3" fill="none" stroke="#d4a82a" stroke-width="1.2"/></svg>
      info@742build.com
    </li>
    <li>
      <svg viewBox="0 0 12 12"><path d="M2.5 0.5l2 2.5-1.2 1.3c.7 1.6 2 2.9 3.6 3.6L8.2 6.7l2.5 2-.9 2C5.2 10.5 1.3 6.6 1 2z"/></svg>
      1-800-555-0142
    </li>
    <li>
      <svg viewBox="0 0 12 12"><g fill="none" stroke="#d4a82a" stroke-width="1"><circle cx="6" cy="6" r="5.2"/><ellipse cx="6" cy="6" rx="2.3" ry="5.2"/><path d="M0.8 6h10.4"/></g></svg>
      www.742build.ca
    </li>
    <li>
      <svg viewBox="0 0 12 12"><path d="M6 0.5a4 4 0 0 1 4 4c0 3-4 7-4 7s-4-4-4-7a4 4 0 0 1 4-4zm0 2.3a1.7 1.7 0 1 0 0 3.4 1.7 1.7 0 0 0 0-3.4z"/></svg>
      18 Harbour Crest Drive
    </li>
    <li class="address-line">Oakridge, Ontario</li>
    <li class="address-line">Canada L0X 2B4</li>
  </ul>
</section>

<section class="card card-back">
  <div class="texture" role="img" aria-label="Subtle debossed square grid pattern on black paper"></div>
  <p class="brand-name">742BUILD</p>
</section>

</body>
</html>
```